New Business Card Design Project

Target Market(s)

Passing cards out

Industry/Entity Type

Asphalt contractor

Contact Information for Business Card

Tallow Creek Paving

Colors
FFC000
F8CF3A
FAE287
FDF2CF
FEFAEE
F0912C
F2A743
F7CA91
FBE8D2
FDF5EE
EE7325
F08F49
F5BC92
FAE3D3
FDF4ED

Requirements
Must have
• Asphalt
Nice to have
• Would like to have 2 pictures on it of equipment

```html
<!DOCTYPE html>
<html lang="en">
<head>
<meta charset="UTF-8">
<title>Tallow Creek Paving – Business Card</title>
<link href="https://fonts.googleapis.com/css2?family=Montserrat:wght@600;700;800&display=swap" rel="stylesheet">
<style>
  :root {
    --backdrop: #2e2e2e;
    --asphalt-dark: #161616;
    --asphalt-mid: #262626;
    --paving-red: #e2231a;
    --paving-red-deep: #a8130e;
    --line-yellow: #f5c518;
    --line-yellow-deep: #c99a0a;
    --ink-white: #ffffff;
    --title-yellow: #f2b21c;
  }
  * { box-sizing: border-box; margin: 0; padding: 0; }
  html, body {
    width: 1200px; height: 800px; overflow: hidden;
    background: var(--backdrop);
    font-family: "Montserrat", Arial, sans-serif;
  }
  .stage { position: relative; width: 1200px; height: 800px; }
  .card {
    position: absolute; left: 280px; width: 640px; height: 366px;
    border-radius: 6px; overflow: hidden;
    background:
      radial-gradient(circle at 30% 20%, rgba(255,255,255,0.06), transparent 60%),
      linear-gradient(160deg, var(--asphalt-mid), var(--asphalt-dark));
    box-shadow: 0 8px 24px rgba(0,0,0,0.45);
  }
  .card--front { top: 24px; }
  .card--back { top: 410px; }

  /* Front */
  .brand-name {
    position: absolute; top: 24px; left: 0; width: 100%;
    text-align: center; color: var(--paving-red);
    font-weight: 800; font-size: 54px; line-height: 60px;
    text-transform: uppercase; letter-spacing: 1px;
  }
  .equipment {
    position: absolute; border-radius: 10px;
  }
  .equipment--truck {
    left: 22px; top: 176px; width: 210px; height: 112px;
    background: linear-gradient(135deg, var(--paving-red), var(--paving-red-deep));
  }
  .equipment--paver {
    right: 24px; top: 156px; width: 200px; height: 118px;
    background: linear-gradient(135deg, var(--line-yellow), var(--line-yellow-deep) 70%, #3a3a3a);
  }
  .stripes { position: absolute; left: 0; top: 0; width: 640px; height: 366px; }

  /* Back */
  .holder-name {
    position: absolute; left: 46px; top: 62px;
    color: var(--ink-white); font-weight: 800; font-size: 32px;
  }
  .holder-title {
    position: absolute; left: 48px; top: 106px;
    color: var(--title-yellow); font-weight: 700; font-size: 16px; letter-spacing: 1.5px;
  }
  .contact-list { position: absolute; left: 48px; top: 146px; list-style: none; }
  .contact-item {
    display: flex; align-items: center; gap: 14px;
    height: 40px; color: var(--ink-white); font-weight: 600; font-size: 19px;
  }
  .contact-icon {
    width: 28px; height: 28px; border-radius: 5px; flex: none;
    background: var(--paving-red);
    display: flex; align-items: center; justify-content: center;
  }
  .contact-icon svg { width: 18px; height: 18px; }
</style>
</head>
<body>
<main class="stage">

  <section class="card card--front">
    <div class="brand-name">Tallow Creek<br>Paving</div>
    <div class="equipment equipment--truck" role="img" aria-label="Illustration of a red dump truck"></div>
    <div class="equipment equipment--paver" role="img" aria-label="Illustration of a yellow asphalt paving machine"></div>
    <svg class="stripes" viewBox="0 0 640 366" aria-hidden="true">
      <polygon points="12,304 196,304 188,324 4,324" fill="var(--paving-red)"/>
      <polygon points="214,304 262,304 254,324 206,324" fill="var(--line-yellow)"/>
      <polygon points="278,304 326,304 318,324 270,324" fill="var(--line-yellow)"/>
      <polygon points="342,304 390,304 382,324 334,324" fill="var(--line-yellow)"/>
    </svg>
  </section>

  <section class="card card--back">
    <div class="holder-name">Daniel Whitcomb</div>
    <div class="holder-title">OWNER</div>
    <ul class="contact-list">
      <li class="contact-item">
        <span class="contact-icon"><svg viewBox="0 0 24 24" fill="#fff"><path d="M6.6 10.8a15.1 15.1 0 0 0 6.6 6.6l2.2-2.2a1 1 0 0 1 1-.25 11.4 11.4 0 0 0 3.6.57 1 1 0 0 1 1 1V20a1 1 0 0 1-1 1A17 17 0 0 1 3 4a1 1 0 0 1 1-1h3.5a1 1 0 0 1 1 1c0 1.25.2 2.45.57 3.57a1 1 0 0 1-.25 1z"/></svg></span>
        (555) 318-6042
      </li>
      <li class="contact-item">
        <span class="contact-icon"><svg viewBox="0 0 24 24" fill="#fff"><path d="M3 5h18v14H3z" fill="none" stroke="#fff" stroke-width="2"/><path d="M3 6l9 7 9-7" fill="none" stroke="#fff" stroke-width="2"/></svg></span>
        daniel@tallowcreekpaving.com
      </li>
      <li class="contact-item">
        <span class="contact-icon"><svg viewBox="0 0 24 24" fill="#fff"><path d="M12 2a7 7 0 0 0-7 7c0 5 7 13 7 13s7-8 7-13a7 7 0 0 0-7-7zm0 9.5A2.5 2.5 0 1 1 12 6.5a2.5 2.5 0 0 1 0 5z"/></svg></span>
        1875 Millstone Road, Waco, TX 76705
      </li>
      <li class="contact-item">
        <span class="contact-icon"><svg viewBox="0 0 24 24" fill="none" stroke="#fff" stroke-width="1.8"><circle cx="12" cy="12" r="9"/><path d="M3 12h18M12 3c3 3 3 15 0 18M12 3c-3 3-3 15 0 18"/></svg></span>
        www.tallowcreekpaving.com
      </li>
    </ul>
    <svg class="stripes" viewBox="0 0 640 366" aria-hidden="true">
      <polygon points="0,318 226,318 214,340 0,340" fill="var(--paving-red)"/>
      <polygon points="240,318 360,318 348,340 228,340" fill="var(--line-yellow)"/>
      <polygon points="376,318 520,318 508,340 364,340" fill="var(--line-yellow)"/>
      <polygon points="470,290 640,198 640,216 500,290" fill="var(--line-yellow)"/>
      <polygon points="520,318 640,250 640,270 552,318" fill="var(--line-yellow)"/>
      <polygon points="566,318 640,278 640,318" fill="var(--paving-red)"/>
    </svg>
  </section>

</main>
</body>
</html>
```